TALBRIDGE VENTORA

I'D LIKE TO REDESIGN MY WEBSITE TO MATCH WITH THE NEW BROCHURE WHICH IS ATTACHED. CONTENT AND LOGOS ARE ATTACHED. PLEASE USE WATCH BRAND LOGOS FROM THE BROCHURE
Coded - Design and coding required
1 page

```html
<!DOCTYPE html>
<html lang="en">
<head>
<meta charset="utf-8">
<title>Talbridge Ventora – International luxury timepiece supplier</title>
<link rel="stylesheet" href="https://fonts.googleapis.com/css2?family=Marcellus&family=Poppins:wght@300;400;500;600;700&display=swap">
<style>
:root{
  --bg:#000000;
  --bg-footer:#0c0c0c;
  --field:#151515;
  --text:#ffffff;
  --text-soft:#c9c9c9;
  --text-dim:#9a9a9a;
  --gold:#c9a94a;
  --gold-light:#e6d37a;
  --gold-dark:#b8973e;
  --rule:#262626;
  --accent:#e8b93c;
}
*{box-sizing:border-box;margin:0;padding:0}
html,body{width:1200px;height:3339px;overflow:hidden;background:var(--bg)}
body{position:relative;font-family:"Poppins",sans-serif;color:var(--text)}
.abs{position:absolute}
.serif{font-family:"Marcellus",serif;font-weight:400}

/* header */
.brand{position:absolute;display:flex;align-items:center;gap:16px}
.brand-mark{width:119px;height:86px;background:linear-gradient(135deg,#2a2410,#6b5a26 55%,#2a2410);border:2px solid var(--gold-dark)}
.brand-name{font-family:"Marcellus",serif;color:var(--text);letter-spacing:2px;white-space:nowrap}
.site-header .brand{left:88px;top:22px}
.site-header .brand-name{font-size:24px}
.main-nav{position:absolute;top:0;left:0;width:1200px;height:120px}
.main-nav a{position:absolute;top:51px;font-size:14px;font-weight:500;color:var(--text);text-decoration:none;letter-spacing:.2px}
.main-nav a.active{color:var(--accent)}
.main-nav .active-bar{position:absolute;top:0;left:608px;width:45px;height:3px;background:var(--accent)}

/* media placeholders */
.media{position:absolute}
.hero-watch{left:557px;top:150px;width:643px;height:470px;background:radial-gradient(ellipse 48% 52% at 50% 50%,#b8a978 0%,#6e6137 35%,#2a2513 62%,rgba(0,0,0,0) 80%)}
.dive-watch{left:149px;top:654px;width:298px;height:473px;background:radial-gradient(ellipse 50% 50% at 50% 50%,#1a1a1a 0%,#1a1a1a 38%,#9a9ea3 42%,#4d5055 62%,rgba(0,0,0,0) 80%)}
.dot-accent{left:634px;top:1095px;width:120px;height:123px;background:linear-gradient(135deg,rgba(201,169,74,.55),rgba(201,169,74,.25))}
.green-watch{left:689px;top:1146px;width:511px;height:531px;background:radial-gradient(ellipse 40% 40% at 52% 48%,#1f7a2c 0%,#175a20 45%,#6f7780 60%,rgba(40,50,65,0) 85%),linear-gradient(120deg,#0a1220 0%,#b9c7d6 55%,#1a2230 100%)}
.sky-watch{left:143px;top:1685px;width:408px;height:430px;background:radial-gradient(ellipse 50% 46% at 50% 42%,#1e2d6a 0%,#2a2a3a 40%,#c9805a 58%,#6a3a22 70%,rgba(0,0,0,0) 80%),linear-gradient(#000 75%,#1f2a5c 100%)}
.steel-watch{left:620px;top:2200px;width:580px;height:545px;background:radial-gradient(ellipse 30% 48% at 37% 50%,#3a3d40 0%,#2c2e30 40%,#c8cacc 55%,#6b6e70 70%,rgba(20,20,20,0) 82%),radial-gradient(ellipse 60% 45% at 55% 45%,#141414 0%,rgba(0,0,0,0) 100%)}

/* hero text */
.hero-kicker{left:90px;top:266px;font-size:20px;color:var(--text-soft);letter-spacing:.5px}
.hero-title{left:88px;top:292px;font-size:72px;line-height:70px;color:var(--text)}
.hero-rule{left:88px;top:454px;width:430px;height:1px;background:var(--gold)}
.hero-sub{left:88px;top:474px;font-size:19px;font-weight:300;color:var(--text-soft)}

/* copy blocks */
.copy p{color:var(--text-soft);font-weight:300}
.intro{left:503px;top:843px;width:560px}
.intro p{font-size:16px;line-height:26.6px;margin-bottom:15px}
.section-title{font-size:46px;line-height:1;color:var(--text);letter-spacing:.5px}
.about-title{left:88px;top:1250px}
.about-copy{left:88px;top:1304px;width:506px}
.about-copy p{font-size:13px;line-height:20.6px;text-align:justify;margin-bottom:18px}
.invest-title{left:626px;top:1864px}
.invest-copy{left:626px;top:1919px;width:450px}
.invest-copy p{font-size:13px;line-height:20.6px;margin-bottom:11px}
.section-rule{left:88px;top:2118px;width:1023px;height:1px;background:var(--rule)}

/* sourcing form */
.source-title{left:131px;top:2208px}
.source-form label{position:absolute;font-size:11px;font-weight:600;color:var(--text);letter-spacing:.2px}
.source-form label span{color:var(--accent)}
.field{position:absolute;background:var(--field);font-size:12.5px;color:var(--text-dim);padding:0 14px;display:flex;align-items:center;justify-content:space-between}
.field svg{width:9px;height:9px}
.field.area{align-items:flex-start;padding-top:18px;padding-left:24px}
.submit-btn{position:absolute;left:133px;top:2681px;width:455px;height:52px;background:linear-gradient(90deg,#b8963d 0%,#d9c062 55%,#e6d574 100%);display:flex;align-items:center;justify-content:center;font-size:18px;font-weight:700;color:#fff;letter-spacing:.3px}
.submit-btn svg{position:absolute;right:22px;top:16px;width:22px;height:20px}

/* footer */
.site-footer{position:absolute;left:0;top:2832px;width:1200px;height:507px;background:var(--bg-footer)}
.footer-brand{left:93px;top:90px;flex-direction:column;gap:14px}
.footer-brand .brand-mark{width:132px;height:94px}
.footer-brand .brand-name{font-size:25px}
.footer-note{left:88px;top:270px;width:300px;font-size:12.5px;line-height:22px;color:var(--text-soft)}
.footer-heading{font-size:21px;color:var(--text);letter-spacing:.3px}
.info-heading{left:456px;top:88px}
.form-heading{left:744px;top:88px}
.info-item{position:absolute;left:456px;display:flex;gap:10px}
.info-item svg{width:13px;height:13px;margin-top:4px;flex:none}
.info-item b{display:block;font-size:12.5px;font-weight:600;color:var(--text)}
.info-item span{display:block;font-size:12.5px;line-height:20px;color:var(--text-soft)}
.ff{position:absolute;background:#1a1a1a;font-size:13px;color:var(--text-soft);padding:0 14px;display:flex;align-items:center}
.ff.area{align-items:flex-start;padding-top:12px}
.send-btn{position:absolute;left:741px;top:334px;width:113px;height:40px;background:linear-gradient(90deg,#b8963d,#d6bd5e);display:flex;align-items:center;justify-content:center;font-size:18px;font-weight:700;color:#fff}
.footer-rule{left:88px;top:447px;width:1023px;height:1px;background:var(--rule)}
.copyright{left:0;top:467px;width:1200px;text-align:center;font-size:12.5px;color:var(--text)}
.to-top{left:1140px;top:427px;width:40px;height:40px;border-radius:50%;background:#262626;display:flex;align-items:center;justify-content:center}
.to-top svg{width:10px;height:10px}
</style>
</head>
<body>

<header class="site-header">
  <div class="brand">
    <div class="brand-mark"></div>
    <div class="brand-name">TALBRIDGE VENTORA</div>
  </div>
  <nav class="main-nav">
    <span class="active-bar"></span>
    <a class="active" style="left:610px">HOME</a>
    <a style="left:681px">ABOUT</a>
    <a style="left:758px">INVESTMENTS</a>
    <a style="left:883px">SEARCH WATCHES</a>
    <a style="left:1041px">CONTACT</a>
  </nav>
</header>

<section class="hero">
  <div class="media hero-watch" role="img" aria-label="Photo of a gold chronograph wristwatch with Roman numeral dial"></div>
  <div class="abs serif hero-kicker">WELCOME TO</div>
  <h1 class="abs serif hero-title">TALBRIDGE<br>VENTORA</h1>
  <div class="abs hero-rule"></div>
  <p class="abs hero-sub">International luxury timepiece supplier</p>
</section>

<section class="intro-section">
  <div class="media dive-watch" role="img" aria-label="Photo of a steel dive watch with black bezel on a bracelet"></div>
  <div class="abs copy intro">
    <p>Simply choose a desired product and allow us to source it for you at the best price and with suitable delivery terms. You will have an option to either collect your purchase from our Cheshire based boutique store, collection points are also in New York City or Dubai or get it delivered to your door via one of our fully insured couriers.</p>
    <p>Making your luxury shopping experience as simple as it can be.</p>
  </div>
</section>

<section class="about">
  <div class="media dot-accent" role="img" aria-label="Gold dotted decorative accent"></div>
  <div class="media green-watch" role="img" aria-label="Photo of a steel dive watch with green dial and bezel, splashed with water"></div>
  <h2 class="abs serif section-title about-title">ABOUT US</h2>
  <div class="abs copy about-copy">
    <p>Talbridge Ventora was first founded in 2018, it has been established as the premier resource to buy and sell premium pre-owned watches. With thousands of watches available from brands including Corvane, Halvet Marchand, Brisset Lorne, Orlan Vey, Sevrin, Maurelle and more, plus international locations and clients there's no better place to find a luxury timepiece.</p>
    <p>Outstanding customer service is a mainstay of the Talbridge Ventora ethos. Watch collectors are discerning shoppers, &amp; will accept nothing but the best, which is why customer service has always will be such an important part of the business.</p>
    <p>Our dedicated team of swiss watch experts are perfectly placed to adapt to the ever changing market conditions, giving our investors an 'out of the box' solution. Longevity is as much a focus as immediate success, ensuring you have the best options we can provide tomorrow as well as</p>
  </div>
</section>

<section class="investments">
  <div class="media sky-watch" role="img" aria-label="Photo of a rose gold skeleton tourbillon watch with planetary globes on a blue strap"></div>
  <h2 class="abs serif section-title invest-title">INVESTMENTS</h2>
  <div class="abs copy invest-copy">
    <p>Interested in becoming part of the ever growing Talbridge Ventora?</p>
    <p>Please leave your details contact form below and one of the team will be in touch to discuss potential options.</p>
  </div>
  <div class="abs section-rule"></div>
</section>

<section class="sourcing">
  <div class="media steel-watch" role="img" aria-label="Photo of a steel sports watch with dual time dial in front of a faint world map"></div>
  <h2 class="abs serif section-title source-title">SOURCING YOUR WATCH</h2>
  <form class="source-form">
    <label style="left:132px;top:2284px">WATCH BRAND<span>*</span></label>
    <div class="field" style="left:132px;top:2303px;width:224px;height:40px">Select brand<svg viewBox="0 0 10 10"><path d="M2 3.5l3 3 3-3" fill="none" stroke="#888" stroke-width="1.2"/></svg></div>
    <label style="left:363px;top:2284px">YEAR<span>*</span></label>
    <div class="field" style="left:363px;top:2303px;width:225px;height:40px">Select year<svg viewBox="0 0 10 10"><path d="M2 3.5l3 3 3-3" fill="none" stroke="#888" stroke-width="1.2"/></svg></div>
    <label style="left:132px;top:2359px">MATERIAL<span>*</span></label>
    <div class="field" style="left:132px;top:2378px;width:224px;height:40px">Enter material<svg viewBox="0 0 10 10"><path d="M2 3.5l3 3 3-3" fill="none" stroke="#888" stroke-width="1.2"/></svg></div>
    <label style="left:363px;top:2359px">BEZEL<span>*</span></label>
    <div class="field" style="left:363px;top:2378px;width:225px;height:40px">Enter bezel<svg viewBox="0 0 10 10"><path d="M2 3.5l3 3 3-3" fill="none" stroke="#888" stroke-width="1.2"/></svg></div>
    <label style="left:132px;top:2434px">STRAP<span>*</span></label>
    <div class="field" style="left:132px;top:2453px;width:456px;height:39px;padding-left:24px">Select strap<svg viewBox="0 0 10 10"><path d="M2 3.5l3 3 3-3" fill="none" stroke="#888" stroke-width="1.2"/></svg></div>
    <label style="left:132px;top:2508px">MESSAGE<span>*</span></label>
    <div class="field area" style="left:132px;top:2527px;width:456px;height:118px">Type your text...</div>
    <div class="submit-btn">SUBMIT NOW<svg viewBox="0 0 24 22"><path d="M1 10L23 1 18 21 11 14z M11 14l12-13" fill="none" stroke="#fff" stroke-width="2" stroke-linejoin="round"/></svg></div>
  </form>
</section>

<footer class="site-footer">
  <div class="brand footer-brand">
    <div class="brand-mark"></div>
    <div class="brand-name">TALBRIDGE VENTORA</div>
  </div>
  <p class="abs footer-note">Alternatively please feel free to contact us on 01615550142 For a more detailed chat with one of our timepiece specialists</p>

  <h3 class="abs serif footer-heading info-heading">CONTACT INFO</h3>
  <div class="info-item" style="top:146px">
    <svg viewBox="0 0 16 16"><path d="M3 1l3 0 1.5 4-2 1.5a9 9 0 0 0 4 4l1.5-2 4 1.5 0 3c0 1-1 2-2 2A14 14 0 0 1 1 3c0-1 1-2 2-2z" fill="var(--accent)"/></svg>
    <div><b>PHONE*</b><span>1615550142</span></div>
  </div>
  <div class="info-item" style="top:197px">
    <svg viewBox="0 0 16 16"><rect x="1" y="3" width="14" height="10" fill="var(--accent)"/><path d="M1 3l7 6 7-6" fill="none" stroke="#0c0c0c" stroke-width="1.4"/></svg>
    <div><b>Email</b><span>sales@talbridgeventora.example</span></div>
  </div>
  <div class="info-item" style="top:249px">
    <svg viewBox="0 0 16 16"><path d="M8 1a5 5 0 0 1 5 5c0 4-5 9-5 9S3 10 3 6a5 5 0 0 1 5-5z" fill="var(--accent)"/><circle cx="8" cy="6" r="1.8" fill="#0c0c0c"/></svg>
    <div><b>Address</b><span>Some address line goes here<br>city name country</span></div>
  </div>

  <h3 class="abs serif footer-heading form-heading">CONTACT FORM</h3>
  <div class="ff" style="left:741px;top:131px;width:182px;height:39px">First Name</div>
  <div class="ff" style="left:932px;top:131px;width:180px;height:39px">Last Name</div>
  <div class="ff" style="left:741px;top:181px;width:182px;height:39px">Phone Number</div>
  <div class="ff" style="left:932px;top:181px;width:180px;height:39px">Email</div>
  <div class="ff area" style="left:741px;top:230px;width:371px;height:87px">Message</div>
  <div class="send-btn">SEND</div>

  <div class="abs footer-rule"></div>
  <div class="abs to-top"><svg viewBox="0 0 10 10"><path d="M2 6.5l3-3 3 3" fill="none" stroke="#fff" stroke-width="1.3"/></svg></div>
  <p class="abs copyright">© Copyright 2022 Talbridge Ventora All Right Reserved</p>
</footer>

</body>
</html>
```